Client Handbook for Modern building company

We are seeking a cover for our client handbook for print and eBook, would like it to be modern and streamlined, this will be a first impression when starting a project for a new client. possibly containing the photo of one of our projects (attached) or something resembling a successful relationship with a client? handshake etc

Requirements
Must have
• Our logo (attached) and our tagline "creating tomorrow" , the words Client Handbook,

```html
<!DOCTYPE html>
<html lang="en">
<head>
<meta charset="utf-8">
<title>Northfield Builders – Client Handbook 2020</title>
<link href="https://fonts.googleapis.com/css2?family=Bebas+Neue&family=Lato:wght@400;700&family=Oswald:wght@400;500&display=swap" rel="stylesheet">
<style>
  :root {
    --page-bg: #f2f2f2;
    --paper: #ffffff;
    --navy: #0b3a58;
    --crimson: #a8121b;
    --teal-top: #0a87a2;
    --teal-bottom: #1a68ab;
    --gold: #f7b955;
    --coral: #ee4f55;
    --sky: #7fb0e0;
    --concrete: #b9bcbf;
    --wood: #5a3a24;
    --wood-dark: #3b2618;
    --white: #ffffff;
  }
  * { margin: 0; padding: 0; box-sizing: border-box; }
  html, body { width: 1034px; height: 1200px; overflow: hidden; background: var(--page-bg); }
  .cover {
    position: absolute; left: 93px; top: 0;
    width: 848px; height: 1200px;
    background: var(--paper);
  }
  .cover-art {
    position: absolute; left: 25px; top: 35px;
    width: 798px; height: 1130px;
    display: block;
  }
  .title { font-family: "Bebas Neue", "Oswald", sans-serif; fill: var(--navy); }
  .subtitle { font-family: "Bebas Neue", "Oswald", sans-serif; fill: var(--crimson); }
  .brand-name { font-family: "Oswald", sans-serif; font-weight: 500; fill: var(--navy); }
  .year { font-family: "Bebas Neue", "Oswald", sans-serif; fill: var(--white); }
  .body-copy { font-family: "Lato", sans-serif; font-size: 12.5px; fill: var(--white); }
  .contact-url { font-family: "Oswald", sans-serif; font-size: 11px; fill: var(--white); }
  .contact-mail { font-family: "Lato", sans-serif; font-size: 13.5px; fill: var(--white); }
  .icon { fill: var(--white); }
</style>
</head>
<body>
<main class="cover">
  <svg class="cover-art" viewBox="0 0 792 1120" preserveAspectRatio="none" xmlns="http://www.w3.org/2000/svg">
    <defs>
      <linearGradient id="houseTone" x1="0" y1="0" x2="0.6" y2="1">
        <stop offset="0" stop-color="var(--sky)"/>
        <stop offset="0.45" stop-color="#6f6a64"/>
        <stop offset="1" stop-color="var(--concrete)"/>
      </linearGradient>
      <linearGradient id="tealTone" x1="0" y1="0" x2="0" y2="1">
        <stop offset="0" stop-color="var(--teal-top)"/>
        <stop offset="1" stop-color="var(--teal-bottom)"/>
      </linearGradient>
      <linearGradient id="deskTone" x1="0" y1="0" x2="1" y2="1">
        <stop offset="0" stop-color="var(--wood)"/>
        <stop offset="1" stop-color="var(--wood-dark)"/>
      </linearGradient>
      <linearGradient id="paperShade" x1="0" y1="0" x2="1" y2="0">
        <stop offset="0" stop-color="#e6e6e6"/>
        <stop offset="0.5" stop-color="#ffffff"/>
      </linearGradient>
    </defs>

    <!-- soft shade between the photo panels -->
    <polygon points="540,0 0,540 0,600 220,335 600,772 792,580 792,0" fill="url(#paperShade)" opacity="0.6"/>

    <!-- completed project photo area -->
    <polygon points="0,0 540,0 0,540" fill="url(#houseTone)" role="img" aria-label="Photo of a completed two-storey modern townhouse with garage and palm"/>

    <!-- teal city panel -->
    <polygon points="0,560 220,335 600,772 252,1120 0,1120" fill="url(#tealTone)" role="img" aria-label="Blue-tinted city skyline reflection"/>

    <!-- client meeting photo area -->
    <polygon points="252,1120 792,580 792,1120" fill="url(#deskTone)" role="img" aria-label="Photo of a handshake over a wooden desk with laptop and paperwork"/>

    <!-- accent stripes -->
    <line x1="402" y1="198" x2="0" y2="598" stroke="var(--gold)" stroke-width="8"/>
    <line x1="82" y1="578" x2="0" y2="663" stroke="var(--coral)" stroke-width="9"/>
    <line x1="792" y1="458" x2="662" y2="593" stroke="var(--coral)" stroke-width="9"/>
    <line x1="792" y1="528" x2="427" y2="893" stroke="var(--gold)" stroke-width="9"/>

    <!-- brand -->
    <g class="brand">
      <circle cx="486" cy="213" r="13" fill="none" stroke="var(--navy)" stroke-width="3"/>
      <text class="brand-name" x="508" y="223" font-size="22" textLength="148" lengthAdjust="spacingAndGlyphs">NORTHFIELD BUILDERS</text>
    </g>

    <!-- title block -->
    <text class="title" x="430" y="324" font-size="126" textLength="256" lengthAdjust="spacingAndGlyphs">CREATING</text>
    <text class="title" x="410" y="422" font-size="126" textLength="320" lengthAdjust="spacingAndGlyphs">TOMORROW</text>
    <text class="subtitle" x="422" y="466" font-size="48" textLength="303" lengthAdjust="spacing">CLIENT HANDBOOK</text>

    <!-- year and highlights -->
    <text class="year" x="126" y="708" font-size="141" textLength="162" lengthAdjust="spacingAndGlyphs">2020</text>

    <g class="highlight">
      <path class="icon" d="M75 751 L75 733 A18 18 0 1 1 59 760 Z"/>
      <path class="icon" d="M71 747 L71 731 A17 17 0 0 0 55 747 Z"/>
      <text class="body-copy" x="130" y="735">Lorem ipsum dolor sit amet, consectetuer</text>
      <text class="body-copy" x="130" y="752">adipiscing elit, sed diam nonummy nibh</text>
      <text class="body-copy" x="130" y="769">euismod</text>
    </g>

    <g class="highlight">
      <circle class="icon" cx="79" cy="809" r="6"/>
      <path class="icon" d="M69 830 a10 11 0 0 1 20 0 Z"/>
      <circle class="icon" cx="64" cy="812" r="5"/>
      <path class="icon" d="M55 830 a9 10 0 0 1 17 -4 l-2 4 Z"/>
      <circle class="icon" cx="94" cy="812" r="5"/>
      <path class="icon" d="M103 830 a9 10 0 0 0 -17 -4 l2 4 Z"/>
      <text class="body-copy" x="130" y="807">Lorem ipsum dolor sit amet, consectetuer</text>
      <text class="body-copy" x="130" y="824">adipiscing elit, sed diam nonummy nibh</text>
      <text class="body-copy" x="130" y="841">euismod</text>
    </g>

    <!-- contact -->
    <g class="contact">
      <path class="icon" d="M60 1021 L71 1031 L68 1031 L68 1044 L52 1044 L52 1031 L49 1031 Z"/>
      <rect x="57" y="1035" width="6" height="9" fill="var(--teal-bottom)"/>
      <text class="contact-url" x="109" y="1042" textLength="134" lengthAdjust="spacingAndGlyphs">WWW.NORTHFIELDBUILDERS.COM</text>

      <rect x="47" y="1059" width="23" height="15" class="icon"/>
      <path d="M47 1059 L58.5 1069 L70 1059 M47 1074 L55 1066 M70 1074 L62 1066" fill="none" stroke="var(--teal-bottom)" stroke-width="1.5"/>
      <text class="contact-mail" x="112" y="1071">hello@northfieldbuilders.com</text>
    </g>
  </svg>
</main>
</body>
</html>
```